childcare program (nursery, preschool, pre-k, and afterschool)

Please, make my website WAY better: brambleweekids.org.
I'm looking for something clean, simple, but impactful that says, "We love child care, because after 20 years, we really do!" Basically, a website that peaks your interest enough to bring you child to. We serve newborns to 12 yr olds, If you take a look at the website you can get an idea of what we use to attract the different age groups. Please be aware that I am open to suggestions.

Target Market(s)

Parents of newborn to 12 year olds

Industry/Entity Type

Childcare

Coding

Coded - Design and coding required

Number of Pages Required

5+ page

Requirements
Must have
• An upgrade to our website that nothing short of an overhaul.
Id like to have an option to have current customers login to pay their tuition. Link to our Chatterloom.
Nice to have
• Something Innovative and different, up to date features in web design.
Something fun and interactive. Think Tobrello from Fennoraldo or Dapple Wisp from Rollo Vane. Also, Testimonials
Should not have
• Traditional, boring

```html
<!DOCTYPE html>
<html lang="en">
<head>
<meta charset="utf-8">
<title>Bramblewee Kids — Childcare</title>
<link rel="stylesheet" href="https://fonts.googleapis.com/css2?family=Fredoka:wght@500;600;700&family=Poppins:wght@400;500;600&family=Patrick+Hand&display=swap">
<style>
:root{
  --navy:#33356b;
  --teal:#36bcb8;
  --teal-dark:#2aa9a5;
  --pink:#f0527f;
  --grey-bg:#eef1f5;
  --soft-bg:#f6f6f7;
  --text:#6d6f7c;
  --white:#ffffff;
  --sky-top:#8fd6ee;
  --sky-bottom:#d4f0f8;
  --footer-ground:#4a7fd6;
}
*{box-sizing:border-box;margin:0;padding:0}
html,body{width:1200px;height:4196px;overflow:hidden;background:var(--white)}
body{font-family:"Poppins",sans-serif;color:var(--text)}
.page{position:relative;width:1200px;height:4196px;overflow:hidden}
.abs{position:absolute}
.display{font-family:"Fredoka",sans-serif;color:var(--navy);font-weight:700}
.script{font-family:"Patrick Hand",cursive}
.btn{position:absolute;display:flex;align-items:center;justify-content:center;border-radius:40px;font-family:"Fredoka",sans-serif;font-weight:700;color:var(--white);font-size:15px;text-decoration:none}
.btn-teal{background:var(--teal)}
.btn-navy{background:var(--navy)}

/* header & hero */
.hero{left:0;top:0;width:1200px;height:597px;background:linear-gradient(90deg,#f4f4f6 0%,#f1f0f1 45%,#e9e3de 100%)}
.hero-photo{left:560px;top:0;width:640px;height:597px;background:radial-gradient(ellipse at 60% 45%,#d8c8b8 0%,#cfc0b0 35%,#e8e1da 75%,rgba(241,240,241,0) 100%)}
.brand{left:163px;top:64px;display:flex;align-items:center;gap:10px}
.brand-dot{width:34px;height:34px;border-radius:50%;background:var(--teal)}
.brand-name{font-family:"Fredoka",sans-serif;font-weight:700;font-size:24px;color:var(--teal)}
.nav{top:73px;left:0;width:1200px;height:20px}
.nav a{position:absolute;font-size:12px;font-weight:500;color:var(--navy);text-decoration:none;letter-spacing:.3px}
.nav .login{top:-7px;padding:6px 14px;border-radius:16px;background:var(--navy);color:var(--white)}
.hero-title{left:129px;top:226px;font-size:52px;line-height:53px}
.hero-btn{top:446px;width:164px;height:47px;font-size:14px}

/* about */
.about-photo{left:67px;top:682px;width:320px;height:329px;background:linear-gradient(160deg,#6f6a86 0%,#9a8a7a 45%,#c3ae8d 100%)}
.trusted{left:299px;top:936px;width:124px;height:124px;border-radius:50%;background:var(--teal);border:5px solid var(--white);display:flex;flex-direction:column;align-items:center;justify-content:center;color:var(--white);font-family:"Fredoka",sans-serif;font-weight:700;font-size:25px;line-height:30px}
.eyebrow{font-size:19px;color:var(--teal)}
.section-title{font-size:44px;line-height:48px}
.body-copy{font-size:12.5px;line-height:26px}

/* services */
.services-bg{left:0;top:1250px;width:1200px;height:492px;background:var(--grey-bg)}
.card{top:1477px;width:308px;height:457px;background:var(--white);box-shadow:0 4px 14px rgba(40,40,80,.08);border-bottom:6px solid var(--teal)}
.card-img{width:308px;height:216px}
.card h3{font-family:"Poppins",sans-serif;font-weight:600;font-size:17px;color:var(--navy);text-align:center;margin-top:22px}
.card p{font-size:11.5px;line-height:19px;color:var(--text);padding:0 32px;margin-top:12px}
.card .read{position:absolute;left:64px;top:395px;width:134px;height:38px;border-radius:20px;background:var(--grey-bg);display:flex;align-items:center;justify-content:center;font-size:13px;color:var(--navy)}

/* call band */
.call-band{left:0;top:2092px;width:1200px;height:363px;background:var(--teal)}
.call-band .script{position:absolute;width:1200px;text-align:center;top:64px;font-size:27px;color:var(--white);letter-spacing:1px}
.call-band h2{position:absolute;width:1200px;text-align:center;font-family:"Fredoka",sans-serif;font-weight:600;color:var(--white);font-size:42px;line-height:54px}

/* mission */
.pause-item{left:708px;display:flex;align-items:center;gap:26px}
.pause-letter{width:58px;height:58px;border-radius:50%;background:var(--teal);color:var(--white);font-family:"Fredoka",sans-serif;font-weight:700;font-size:30px;display:flex;align-items:center;justify-content:center}
.pause-label{font-family:"Fredoka",sans-serif;font-weight:700;font-size:25px;color:var(--navy)}
.testimonial{left:0;top:3030px;width:1200px;text-align:center}
.testimonial q{font-size:15px;color:var(--navy)}
.testimonial span{display:block;margin-top:6px;font-size:12px;color:var(--teal);font-weight:600}

/* contact */
.contact-bg{left:0;top:3118px;width:1200px;height:687px;background:var(--soft-bg)}
.field{background:var(--teal);border-radius:3px;color:var(--white);font-family:"Fredoka",sans-serif;font-weight:600;font-size:12px;padding:18px 17px}

/* footer */
.footer{left:0;top:3805px;width:1200px;height:391px;background:linear-gradient(180deg,var(--sky-top) 0%,var(--sky-bottom) 100%)}
.footer h4{position:absolute;font-family:"Poppins",sans-serif;font-weight:600;font-size:21px;color:var(--navy)}
.footer .link{position:absolute;font-size:13px;color:var(--white)}
.skyline{left:0;top:4090px;width:1200px;height:106px;background:linear-gradient(180deg,rgba(74,127,214,0) 0%,var(--footer-ground) 55%)}
.chat{left:921px;top:4145px;width:264px;height:51px;background:var(--teal-dark);color:var(--white);padding:9px 16px;font-size:12px}
.chat small{display:block;font-size:8px;opacity:.85}
</style>
</head>
<body>
<div class="page">

  <section class="abs hero"></section>
  <div class="abs hero-photo" role="img" aria-label="Photo of a small child in an aviator cap playing with a wooden toy plane beside a teddy bear"></div>

  <div class="abs brand"><span class="brand-dot"></span><span class="brand-name">Bramblewee Kids</span></div>
  <nav class="abs nav">
    <a style="left:620px">HOME</a>
    <a style="left:696px">GALLERY</a>
    <a style="left:790px">CONTACT US</a>
    <a style="left:904px">VIDEOS</a>
    <a style="left:982px">PROGRAMS</a>
    <a class="login" style="left:1075px">PAY TUITION</a>
  </nav>

  <h1 class="abs display hero-title">Together We’ll<br>Explore New<br>Things</h1>
  <a class="btn btn-teal hero-btn" style="left:129px">LEARN MORE</a>
  <a class="btn btn-teal hero-btn" style="left:336px">CONTACT US</a>

  <div class="abs about-photo" role="img" aria-label="Photo of teachers and children doing a paper craft activity at a table"></div>
  <div class="abs trusted"><span>Trusted</span><span>100%</span></div>

  <p class="abs script eyebrow" style="left:640px;top:706px">Welcome to Bramblewee Kids</p>
  <h2 class="abs display section-title" style="left:637px;top:746px">What we do?</h2>
  <svg class="abs" style="left:640px;top:802px" width="72" height="10" viewBox="0 0 72 10"><path d="M2 7 Q8 1 14 7 T26 7 T38 7 T50 7 T62 7 T72 7" fill="none" stroke="var(--pink)" stroke-width="2.5"/></svg>
  <p class="abs body-copy" style="left:638px;top:850px;width:420px">We strive to provide a safe learning environment that will inspire each child in our care to explore and grow at his or her own pace. Our team of administrators, teachers, and caregivers spend time nurturing your children’s strengths while encouraging them to reach new heights.</p>
  <a class="btn btn-teal" style="left:628px;top:1055px;width:164px;height:47px">Discover Now</a>

  <div class="abs services-bg"></div>
  <h2 class="abs display" style="left:0;top:1348px;width:1200px;text-align:center;font-size:46px">Services We Offer</h2>

  <article class="abs card" style="left:117px">
    <div class="card-img" role="img" aria-label="Photo of a mother holding her toddler" style="background:linear-gradient(150deg,#3a2a22 0%,#7a5640 50%,#c9d4de 100%)"></div>
    <h3>Nursery and Toddlers</h3>
    <p>We believe that the best place for your baby is in your arms. But being that most homes today contain two “breadwinners”, the very next best thing is in the loving arms of our caring staff.</p>
    <span class="read">Read More</span>
  </article>
  <article class="abs card" style="left:449px">
    <div class="card-img" role="img" aria-label="Photo of preschoolers sitting on red chairs listening to a story" style="background:linear-gradient(160deg,#8d7a6d 0%,#b8473f 55%,#d9d1c8 100%)"></div>
    <h3>Pre-K</h3>
    <p>As your child grows, so does his curiosity meter. Your toddler absorbs information like a sponge at this stage. At this stage we will also begin the process of reading, writing, and math readiness.</p>
    <span class="read">Read More</span>
  </article>
  <article class="abs card" style="left:781px">
    <div class="card-img" role="img" aria-label="Photo of a schoolboy writing with a pencil" style="background:linear-gradient(160deg,#c79a6a 0%,#7a4a2e 50%,#e6c9a3 100%)"></div>
    <h3>After School Programs</h3>
    <p>Our Pre-Kers never stop exploring, and are introduced to problem-solving concepts that involve math and science. Our curriculum also focuses on reading through sight words and word recognition.</p>
    <span class="read">Read More</span>
  </article>

  <a class="btn btn-navy" style="left:518px;top:1991px;width:198px;height:41px;font-size:16px">View All Programs</a>

  <section class="abs call-band">
    <p class="script">Three amazing locations to serve you.</p>
    <h2 style="top:112px">Call To Enrol Your Child</h2>
    <h2 style="top:168px">555 014 0388</h2>
    <a class="btn btn-navy" style="left:500px;top:267px;width:255px;height:59px;font-size:18px">All Programs</a>
  </section>

  <p class="abs script eyebrow" style="left:138px;top:2604px">Welcome to Bramblewee Kids</p>
  <h2 class="abs display section-title" style="left:131px;top:2642px">Our mission at<br>Bramblewee Kids</h2>
  <p class="abs body-copy" style="left:138px;top:2780px;width:420px">We believe that every child is unique and we believe that success and growth come from encouragement and praise. Our teachers focus on building every child’s self esteem and confidence through P.A.U.S.E:</p>
  <a class="btn btn-teal" style="left:132px;top:2922px;width:164px;height:48px">Discover Now</a>

  <div class="abs pause-item" style="top:2585px"><span class="pause-letter">P</span><span class="pause-label">Physical Play</span></div>
  <div class="abs pause-item" style="top:2670px"><span class="pause-letter">A</span><span class="pause-label">Academia</span></div>
  <div class="abs pause-item" style="top:2757px"><span class="pause-letter">U</span><span class="pause-label">Unconditional Love</span></div>
  <div class="abs pause-item" style="top:2846px"><span class="pause-letter">S</span><span class="pause-label">Safety</span></div>
  <div class="abs pause-item" style="top:2936px"><span class="pause-letter">E</span><span class="pause-label">Edification</span></div>

  <blockquote class="abs testimonial"><q>Our daughter runs in every morning. The teachers truly feel like family to us.</q><span>— A Bramblewee Kids parent</span></blockquote>

  <div class="abs contact-bg"></div>
  <h2 class="abs display" style="left:0;top:3187px;width:1200px;text-align:center;font-size:46px">Contact Us</h2>
  <div class="abs field" style="left:326px;top:3280px;width:299px;height:60px">First Name</div>
  <div class="abs field" style="left:647px;top:3280px;width:301px;height:60px">Last Name</div>
  <div class="abs field" style="left:326px;top:3360px;width:299px;height:60px">Email</div>
  <div class="abs field" style="left:647px;top:3360px;width:301px;height:60px">Phone</div>
  <div class="abs field" style="left:326px;top:3442px;width:622px;height:68px">Address</div>
  <div class="abs field" style="left:326px;top:3530px;width:622px;height:97px">Type your message here</div>
  <a class="btn btn-navy" style="left:527px;top:3663px;width:188px;height:46px;font-family:'Poppins',sans-serif;font-weight:400;font-size:12px">Submit</a>

  <footer class="abs footer">
    <h4 style="left:418px;top:58px">Our Programs</h4>
    <span class="link" style="left:430px;top:109px">After School Program</span>
    <span class="link" style="left:430px;top:148px">Pre-K</span>
    <span class="link" style="left:430px;top:187px">Nursery and Toddlers</span>
    <span class="link" style="left:430px;top:231px">After School Program</span>

    <h4 style="left:686px;top:58px">Contact Us</h4>
    <svg class="abs" style="left:651px;top:112px" width="40" height="46" viewBox="0 0 40 46"><path d="M20 3C11 3 5 10 5 18c0 11 15 25 15 25s15-14 15-25C35 10 29 3 20 3z" fill="none" stroke="var(--pink)" stroke-width="3"/><circle cx="20" cy="18" r="6" fill="none" stroke="var(--pink)" stroke-width="3"/></svg>
    <span class="link" style="left:715px;top:114px;font-size:12px;line-height:16px;width:170px">27 Harrow Lane Fernvale,<br>NY 10990 US</span>
    <svg class="abs" style="left:650px;top:188px" width="42" height="30" viewBox="0 0 42 30"><rect x="1" y="1" width="40" height="28" rx="2" fill="var(--pink)"/><path d="M2 3l19 14 19-14" fill="none" stroke="var(--white)" stroke-width="2"/></svg>
    <span class="link" style="left:722px;top:195px;font-size:12px">hello@brambleweekids.org</span>
    <svg class="abs" style="left:651px;top:248px" width="40" height="40" viewBox="0 0 40 40"><path d="M9 4l7 8-4 5c3 6 7 10 13 13l5-4 8 7-5 5C20 37 3 20 4 9z" fill="none" stroke="var(--pink)" stroke-width="2.5" stroke-linejoin="round"/></svg>
    <span class="link" style="left:725px;top:257px;font-size:12px;text-decoration:underline">5550140388</span>

    <h4 style="left:924px;top:58px">Newsletter</h4>
    <span class="link" style="left:930px;top:117px;width:200px;font-size:12px;line-height:15px">Subscribe Our Newsletters To Get More Update</span>
    <div class="abs" style="left:928px;top:172px;width:203px;height:36px;background:var(--white);padding:10px 22px;font-size:11px;color:var(--pink)">Email</div>
    <div class="abs" style="left:938px;top:247px;width:140px;height:38px;background:var(--pink);color:var(--white);font-size:12px;font-weight:500;display:flex;align-items:center;justify-content:center">Submit</div>
  </footer>
  <div class="abs skyline" role="img" aria-label="Illustration of a town skyline with houses and trees along the bottom edge"></div>
  <div class="abs chat">CHAT WITH US<small>We’ll reply as soon as we can</small></div>

</div>
</body>
</html>
```